Business Card Design For A Renovation Contractor Company

We need a business card for a new company based in Singapore, our company name is "KT Planora". We are a renovation contractor that builds designs into reality. We build more of F&B restaurants, retail stores and commercial offices. We work very closely with designers. The final design should communicate to our client that we are a company that you can trust, that will plan and complete your project without giving you a headache. I like my client to remember my company as "KT". The beauty of SIMPLE is important.

Industry/Entity Type

Contractor

Requirements
Nice to have
• Black or Red base

```html
<!DOCTYPE html>
<html lang="en">
<head>
<meta charset="utf-8">
<title>KT Planora – Business Card</title>
<link rel="stylesheet" href="https://fonts.googleapis.com/css2?family=Arimo:wght@400;700&family=Tinos:wght@400&display=swap">
<style>
  :root {
    --stage: #b9b9b9;
    --brand-red: #d1171f;
    --ink: #2a2a2a;
    --ink-soft: #6b6b6b;
    --paper: #f4f4f2;
    --white: #ffffff;
  }
  * { box-sizing: border-box; margin: 0; padding: 0; }
  html, body {
    width: 1200px; height: 900px; overflow: hidden;
    background: var(--stage);
  }
  .stage {
    width: 1200px; height: 900px;
    display: flex; align-items: center; justify-content: center; gap: 40px;
  }
  .card {
    position: relative;
    width: 540px; height: 310px;
    border-radius: 26px;
    overflow: hidden;
  }

  /* Back side */
  .card-back { background: var(--brand-red); color: var(--white); }
  .tagline-stack {
    position: absolute; left: 70px; top: 66px;
    font-family: "Arimo", Arial, sans-serif; line-height: 1;
  }
  .tagline-small { font-size: 26px; color: var(--ink); display: block; }
  .tagline-large { font-size: 66px; color: var(--white); display: block; letter-spacing: -1px; }
  .tagline-row { display: flex; align-items: baseline; gap: 12px; }
  .tagline-stack .tagline-small.first { margin-left: 4px; margin-bottom: -4px; }
  .tagline-stack .tagline-large.second { margin-bottom: -6px; }
  .tagline-row .tagline-small { margin-left: 14px; }
  .web-address {
    position: absolute; right: 40px; bottom: 66px;
    font-family: "Tinos", "Times New Roman", serif; font-size: 17px; color: var(--white);
  }

  /* Front side */
  .card-front { background: var(--paper); }
  .edge-dot {
    position: absolute; left: -9px; top: 52px;
    width: 18px; height: 18px; border-radius: 50%; background: var(--brand-red);
  }
  .holder { position: absolute; left: 48px; top: 46px; font-family: "Tinos", "Times New Roman", serif; }
  .holder-name { font-size: 21px; color: var(--ink-soft); letter-spacing: .5px; }
  .holder-role { font-size: 17px; color: var(--brand-red); margin-top: 2px; }
  .contact-list {
    position: absolute; left: 48px; top: 152px; list-style: none;
    font-family: "Tinos", "Times New Roman", serif; font-size: 15.5px; color: var(--ink-soft); line-height: 1.25;
  }
  .contact-list li { display: flex; align-items: flex-start; gap: 10px; margin-bottom: 1px; }
  .contact-list svg { width: 12px; height: 12px; margin-top: 3px; flex: none; fill: var(--brand-red); }
  .brand-block {
    position: absolute; right: 40px; top: 128px; width: 250px;
    display: flex; flex-direction: column; align-items: center;
  }
  .brand-mark {
    width: 62px; height: 62px; border-radius: 50%; background: var(--brand-red);
    margin-bottom: 12px;
  }
  .brand-name {
    font-family: "Arimo", Arial, sans-serif; font-size: 44px; color: var(--ink);
    letter-spacing: -.5px; line-height: 1;
  }
  .brand-rule { width: 250px; height: 1.5px; background: var(--ink); margin: 6px 0 4px; }
  .brand-tagline { font-family: "Arimo", Arial, sans-serif; font-size: 17px; color: var(--ink); }
</style>
</head>
<body>
<main class="stage">
  <section class="card card-back" aria-label="Card back">
    <div class="tagline-stack">
      <span class="tagline-small first">shaping</span>
      <span class="tagline-large second">spaces</span>
      <div class="tagline-row">
        <span class="tagline-small">with</span>
        <span class="tagline-large">care</span>
      </div>
    </div>
    <p class="web-address">www.ktplanora.com</p>
  </section>

  <section class="card card-front" aria-label="Card front">
    <span class="edge-dot"></span>
    <div class="holder">
      <p class="holder-name">CARDHOLDER NAME</p>
      <p class="holder-role">Designation</p>
    </div>
    <ul class="contact-list">
      <li>
        <svg viewBox="0 0 12 12"><path d="M6 0a4 4 0 0 1 4 4c0 3-4 8-4 8S2 7 2 4a4 4 0 0 1 4-4zm0 2.4a1.6 1.6 0 1 0 0 3.2 1.6 1.6 0 0 0 0-3.2z"/></svg>
        <span>01 01 Avenue, Suite No. 123<br>Your City, Country</span>
      </li>
      <li>
        <svg viewBox="0 0 12 12"><circle cx="6" cy="6" r="6"/><path d="M4 3l1.2 1.4-.6.8c.5 1 1.2 1.7 2.2 2.2l.8-.6L9 8l-1 1.2C5.5 9 3 6.5 2.8 4z" fill="#fff"/></svg>
        <span>012 345 6789</span>
      </li>
      <li>
        <svg viewBox="0 0 12 12"><rect x="3" y="0" width="6" height="4"/><rect x="1" y="5" width="10" height="7" rx="1"/></svg>
        <span>012 345 6780</span>
      </li>
      <li>
        <svg viewBox="0 0 12 12"><rect x="0" y="2" width="12" height="8" rx="1"/><path d="M1 3l5 3.5L11 3" stroke="#fff" fill="none"/></svg>
        <span>name@ktplanora.com</span>
      </li>
    </ul>
    <div class="brand-block">
      <span class="brand-mark"></span>
      <p class="brand-name">KT Planora</p>
      <span class="brand-rule"></span>
      <p class="brand-tagline">shaping spaces with care</p>
    </div>
  </section>
</main>
</body>
</html>
```